TRVL-NINE Web Design

We are a Health, Safety, Environmental & Quality Recruitment Agency, our clients are major corporate Mining, Oil & Gas and Engineering companies. We have offices in Perth & Melbourne, Australia

The website should be very functional & easy to navigate

BUT REALLY LOOKING FOR WOW FACTOR!

Please Note: TRVL CORPORATE IS OUR OLD COMPANY THE NEW ONE IS "TRVL-NINE" 

Some idea's from our competitors:

http://www.guardlinepeak.com.au/
http://www.vantagehiring.com.au/
http://www.brightpick.com.au/
http://www.kovastaffing.co.uk/
http://www.jobmarrow.com/health-safety-environment-jobs

Would love to see some of our valued clients and there logos

still looking for wow factor

Industry/Entity Type

Mining

Requirements
Must have
• A place where candidates can upload there resumes & other contact details
• eg: http://www.guardlinepeak.com.au/candidates/register-your-resume/
• A place we can load jobs on to eg: http://www.guardlinepeak.com.au/vacancies/
• Contact details:
• Perth: 12 Kestrel Ave, West Perth, Western Australia 6005
• t: 08 7153 4406 | f: 08 7153 4470 |
• Melbourne: Level 1, 218 Arbour Lane, Melbourne, Victoria 3000
• t: 03 6214 5072| f: 03 6231 4095 |
• e: dennisk@trvlnine.com.au | w: http://www.trvlnine.com.au

```html
<!DOCTYPE html>
<html lang="en">
<head>
<meta charset="utf-8">
<title>TRVL-NINE | Health, Safety, Environment &amp; Quality Recruitment</title>
<link rel="stylesheet" href="https://fonts.googleapis.com/css2?family=Lato:wght@300;400;700&display=swap">
<style>
:root{
  --blue:#1a9ad6;
  --ink:#2b2b2b;
  --body:#555;
  --rule:#e3e6ea;
  --footer:#232325;
  --footer-text:#b9b9b9;
  --footer-muted:#8a8a8a;
  --red:#d0161b;
  --panel:#e9ecf2;
}
*{box-sizing:border-box;margin:0;padding:0}
html,body{width:1029px;height:1200px;overflow:hidden}
body{position:relative;font-family:'Lato',sans-serif;color:var(--ink);background:#fff}
.abs{position:absolute}
.top-band{left:0;top:0;width:1029px;height:310px;background:linear-gradient(#fff 0%,var(--panel) 100%);border-bottom:1px solid #dfe3ea}
.logo{left:168px;top:20px;display:flex;align-items:center;gap:10px}
.logo-mark{width:54px;height:54px;background:#5b7a93}
.logo-name{font-size:30px;font-weight:300;color:var(--blue);letter-spacing:1px}
.phone{right:175px;top:14px;font-size:20px;font-weight:700;color:var(--blue);letter-spacing:-.5px}
.email{right:175px;top:42px;font-size:8.5px;color:#333;display:flex;align-items:center;gap:6px}
.email svg{display:block}
.nav{right:251px;top:67px;display:flex;gap:5px;font-size:9.5px;text-transform:uppercase;color:#222;white-space:nowrap}
.nav .sep{color:#999}
.nav .active{position:relative}
.nav .active::after{content:"";position:absolute;left:-2px;right:-2px;top:14px;height:3px;background:var(--blue)}
.social{left:791px;top:65px;display:flex;gap:9px;padding-left:9px;border-left:1px dotted #9cc}
.social span{width:11px;height:11px;background:var(--blue);display:block}
.slider{left:166px;top:93px;width:688px;height:302px;background:#fff;padding:5px;box-shadow:0 1px 6px rgba(0,0,0,.25)}
.slider .photo{width:100%;height:100%;background:linear-gradient(90deg,#25345a 0%,#8ea0b8 45%,#cfd7e2 70%,#6f7e92 100%)}
.dots{left:486px;top:407px;display:flex;gap:2px}
.dots span{width:9px;height:9px;border-radius:50%;background:#777}
.dots span:first-child{background:var(--blue)}
.service{top:450px;width:212px}
.service h2{font-size:18px;font-weight:400;color:#333;padding-bottom:8px;border-bottom:2px solid var(--rule);position:relative}
.service h2::after{content:"";position:absolute;left:0;bottom:-2px;width:31px;height:2px;background:var(--blue)}
.service .photo{margin-top:14px;height:124px;border:3px solid #eee}
.service p{margin-top:14px;font-size:9.4px;line-height:12.6px;color:#444}
.more{margin-top:4px;font-size:9.5px;font-weight:700;color:var(--blue);display:flex;align-items:center;gap:5px}
.more i{width:11px;height:11px;border-radius:50%;background:#ccc;display:block}
.offer{left:168px;top:722px;width:686px}
.offer h1{font-size:25px;font-weight:300;color:var(--blue);letter-spacing:-.3px}
.offer h3{font-size:19px;font-weight:400;color:#222;margin-top:2px;letter-spacing:-.3px}
.offer .rule{margin-top:10px;height:2px;background:var(--rule);position:relative}
.offer .rule::after{content:"";position:absolute;left:0;top:0;width:50px;height:2px;background:var(--blue)}
.areas{top:815px;list-style:none}
.areas li{height:26px;font-size:13px;font-weight:300;color:#333;display:flex;align-items:center;gap:8px}
.areas li::before{content:"";width:12px;height:12px;border-radius:50%;background:#bfe3f5;flex:none}
.complete{left:169px;top:940px;font-size:14px;color:#222;letter-spacing:-.2px}
.complete a{color:var(--red);font-size:10.5px;text-decoration:none}
.footer{left:0;top:1004px;width:1029px;height:196px;background:var(--footer)}
.office{top:1032px;color:var(--footer-text);font-size:8.6px;line-height:13.5px}
.office h4{font-size:16px;font-weight:700;color:#fff;letter-spacing:-.5px;line-height:18px;margin-bottom:8px}
.office .contact{margin-top:4px;color:var(--footer-muted)}
.badge{top:1060px;width:83px;height:66px}
.badge.light{left:683px;background:#fff}
.badge.purple{left:771px;background:#5a3a96}
.foot-social{left:684px;top:1133px;display:flex;gap:3px}
.foot-social span{width:18px;height:18px;border-radius:50%;background:#fff;display:block}
.legal{left:168px;top:1170px;font-size:9.5px;color:#c8c8c8}
.copyright{right:175px;top:1169px;font-size:10.5px;color:#bbb}
</style>
</head>
<body>
<div class="abs top-band"></div>

<header>
  <div class="abs logo">
    <span class="logo-mark"></span>
    <span class="logo-name">trvlnine</span>
  </div>
  <div class="abs phone">01632 96 04 18</div>
  <div class="abs email">
    <svg width="14" height="10" viewBox="0 0 14 10"><rect width="14" height="10" fill="#1a9ad6"/><path d="M1 1l6 5 6-5" stroke="#fff" fill="none" stroke-width="1.2"/></svg>
    <span>SALES@TRVLNINE.COM</span>
  </div>
  <nav class="abs nav">
    <span class="active">Home</span><span class="sep">/</span>
    <span>About Us</span><span class="sep">/</span>
    <span>Positions We Offer</span><span class="sep">/</span>
    <span>Candidates</span><span class="sep">/</span>
    <span>Employers</span>
  </nav>
  <div class="abs social">
    <span></span><span></span>
    <svg width="11" height="11" viewBox="0 0 11 11"><circle cx="1.5" cy="9.5" r="1.5" fill="#1a9ad6"/><path d="M0 5a6 6 0 0 1 6 6M0 1a10 10 0 0 1 10 10" stroke="#1a9ad6" stroke-width="1.8" fill="none"/></svg>
  </div>
</header>

<section class="abs slider">
  <div class="photo" role="img" aria-label="Worker in hard hat on a phone in front of an oil refinery"></div>
</section>
<div class="abs dots"><span></span><span></span><span></span><span></span><span></span><span></span></div>

<article class="abs service" style="left:168px">
  <h2>Health Recruitment</h2>
  <div class="photo" role="img" aria-label="Two site workers in hard hats reviewing a clipboard" style="background:linear-gradient(90deg,#c8d8ea,#8fb0d0 50%,#2c3f72)"></div>
  <p>Custom Admin Panel Significantly Extends Original Sitepress Functionality, Turning It Into An All-in-one Tool For Content Management.</p>
  <div class="more"><i></i>Read More</div>
</article>
<article class="abs service" style="left:400px">
  <h2>Safety Recruitment</h2>
  <div class="photo" role="img" aria-label="Business people shaking hands at a trade exhibition" style="background:linear-gradient(90deg,#e3b23a,#9db3c6 45%,#e4d8c8)"></div>
  <p>Custom Admin Panel Significantly Extends Original Sitepress Functionality, Turning It Into An All-in-one Tool For Content Management.</p>
  <div class="more"><i></i>Read More</div>
</article>
<article class="abs service" style="left:636px">
  <h2>Quality Recruitment</h2>
  <div class="photo" role="img" aria-label="Miner holding a piece of metallic ore" style="background:linear-gradient(90deg,#1a1a1a,#6f5a4a 45%,#b99470 80%,#d7b24a)"></div>
  <p>Custom Admin Panel Significantly Extends Original Sitepress Functionality, Turning It Into An All-in-one Tool For Content Management.</p>
  <div class="more"><i></i>Read More</div>
</article>

<section class="abs offer">
  <h1>Offering Both Contract And Permanent Placements</h1>
  <h3>Our Areas Of Recruitment Include</h3>
  <div class="rule"></div>
</section>

<ul class="abs areas" style="left:168px">
  <li>OHS Officers</li><li>Safety Advisors</li><li>Occupational Hygienists</li><li>Training Advisors</li>
</ul>
<ul class="abs areas" style="left:394px">
  <li>Quality Control Specialists</li><li>QAQC Engineers</li><li>Project Quality Managers</li><li>Environmental Officers</li>
</ul>
<ul class="abs areas" style="left:629px">
  <li>Training Superintendents</li><li>Training Managers</li><li>Environmental Scientists</li><li>Corporate Environmental Managers</li>
</ul>

<p class="abs complete">For The Complete List Of Positions We Offer, <a href="#">( Click Here )</a></p>

<footer>
  <div class="abs footer"></div>
  <div class="abs office" style="left:168px">
    <h4>Perth Office</h4>
    Suite 4, 62 Harlow Road<br>Subiaco<br>Western Australia 6008
    <div class="contact">P | +61 (0) 8 7240 1183<br>F | +61 (0) 8 7240 1190<br>E | info@trvlcorp.com.au</div>
  </div>
  <div class="abs office" style="left:343px">
    <h4>Brisbane Office</h4>
    Level 21, Meridian Plaza<br>127 Tallow Street, Brisbane<br>Queensland 4000
    <div class="contact">P | +61 (0) 7 4180 2257<br>F | +61 (0) 7 4180 2290<br>E | info@trvlcorp.com.au</div>
  </div>
  <div class="abs office" style="left:509px;top:1031px">
    <h4>Seoul Office</h4>
    Level 33, Harbour Trade Tower<br>208 Hanbit-ro<br>Samsung dong, Gangnam-Gu<br>Seoul, Republic of Korea
    <div class="contact">P | +82 (0) 2 5140 3382<br>F | +82 (0) 2 5140 3300<br>E | minjik@trvlcorp.com.au</div>
  </div>
  <div class="abs office" style="left:686px"><h4>Corporate Members</h4></div>
  <div class="abs badge light"></div>
  <div class="abs badge purple"></div>
  <div class="abs foot-social"><span></span><span></span><span></span></div>
  <div class="abs legal">HOME | RSS FEED | LOGIN | REGISTER | PRIVACY POLICY | LEGAL | TESTIMONIALS</div>
  <div class="abs copyright">Copyright © 2013 TRVL-NINE All Rights Reserved.</div>
</footer>
</body>
</html>
```